PVTR - Label for a lifestyle beer for gamers

We are launching a lifestyle brewery for gamers. Our first beer is called PVTR (the same as the company) and we are launching a promo campaign showcasing a bunch of possible design directions for it, which our community can then vote for. The top 5 (or more) labels of this competition will be selected as winners and be part of that campaign. If one of them is chosen by the community, we will continue that work with the chosen designer.

So feel free to come up with a specific game genre, target group (described in the attachment) or style for your submission. Or a specific market (such as a Korvaxi inspired beer for the japanese market) We encourage diversity among the submissions.

Full description in the attached document.

Target Market(s)

Gamers of all ages

Requirements
Nice to have
• All kinds of gaming references or graphical choices inspired by gaming

```html
<!DOCTYPE html>
<html lang="en">
<head>
<meta charset="utf-8">
<title>PVTR Pale Ale – label directions</title>
<link rel="stylesheet" href="https://fonts.googleapis.com/css2?family=Bebas+Neue&family=Press+Start+2P&family=Silkscreen:wght@700&display=swap">
<style>
  :root {
    --backdrop: #e9e9eb;
    --orange-deep: #e8870c;
    --orange: #f39c14;
    --amber: #f8bd22;
    --lemon: #f7e23a;
    --navy: #1d2a5c;
    --royal: #1f4f9a;
    --white: #ffffff;
    --hop-tint: rgba(214, 110, 20, 0.35);
  }
  * { box-sizing: border-box; margin: 0; padding: 0; }
  html, body { width: 1034px; height: 1200px; overflow: hidden; }
  body { background: var(--backdrop); position: relative; }

  .label {
    position: absolute;
    top: 150px;
    width: 400px;
    height: 900px;
    overflow: hidden;
    text-align: center;
  }
  .label--classic {
    left: 70px;
    background:
      radial-gradient(ellipse 45% 30% at 50% 42%, rgba(247, 226, 58, 0.9), rgba(247, 226, 58, 0) 100%),
      linear-gradient(90deg, var(--orange-deep), var(--amber) 45%, var(--orange) 80%, var(--orange-deep));
  }
  .label--pixel {
    left: 564px;
    background: linear-gradient(90deg, var(--orange), var(--amber) 40%, var(--amber) 60%, var(--orange));
  }

  .decor {
    position: absolute;
    background: var(--hop-tint);
    border-radius: 40%;
  }
  .decor--hop-top { right: -20px; top: 80px; width: 60px; height: 110px; }
  .decor--mug-left { left: -14px; top: 520px; width: 56px; height: 90px; border-radius: 8px; }
  .decor--hop-mid { right: -16px; top: 400px; width: 50px; height: 100px; }
  .decor--mug-right { right: -10px; top: 620px; width: 50px; height: 110px; border-radius: 8px; }
  .decor--hop-low { left: -14px; top: 700px; width: 50px; height: 110px; }

  .skyline {
    position: absolute;
    left: 0; right: 0;
    top: 400px;
    height: 75px;
    background: rgba(240, 150, 20, 0.35);
  }

  .brand {
    position: absolute;
    left: 0; right: 0;
    top: 225px;
    font-family: "Bebas Neue", sans-serif;
    font-size: 150px;
    line-height: 1;
    color: var(--royal);
    letter-spacing: 6px;
  }

  .tagline {
    position: absolute;
    left: 0; right: 0;
    top: 368px;
    font-family: "Press Start 2P", monospace;
    font-size: 12px;
    color: var(--white);
    letter-spacing: 1px;
    word-spacing: 4px;
    text-shadow: 1px 1px 0 rgba(29, 42, 92, 0.6);
  }

  .style-name,
  .product {
    position: absolute;
    left: 0; right: 0;
    color: var(--white);
  }
  .label--classic .style-name {
    top: 545px;
    font-family: "Bebas Neue", sans-serif;
    font-size: 82px;
    line-height: 1;
    text-shadow: 3px 3px 0 var(--navy);
  }
  .label--classic .product {
    top: 628px;
    font-family: "Bebas Neue", sans-serif;
    font-size: 145px;
    line-height: 1;
    letter-spacing: 10px;
    padding-left: 10px;
    text-shadow: 4px 4px 0 var(--navy);
  }
  .label--pixel .style-name {
    top: 560px;
    font-family: "Silkscreen", sans-serif;
    font-weight: 700;
    font-size: 44px;
    line-height: 1;
    text-shadow: 4px 4px 0 var(--navy);
  }
  .label--pixel .product {
    top: 640px;
    font-family: "Silkscreen", sans-serif;
    font-weight: 700;
    font-size: 86px;
    line-height: 1;
    text-shadow: 5px 5px 0 var(--navy);
  }

  .strength {
    position: absolute;
    left: 0; right: 0;
    top: 842px;
    font-family: "Bebas Neue", sans-serif;
    font-size: 32px;
    letter-spacing: 2px;
    color: var(--navy);
  }
  .label--pixel .strength { color: var(--royal); }
</style>
</head>
<body>

  <section class="label label--classic">
    <div class="decor decor--hop-top" role="img" aria-label="Faint hop cone illustration"></div>
    <div class="decor decor--mug-left" role="img" aria-label="Faint pixel beer mug illustration"></div>
    <div class="decor decor--hop-mid" role="img" aria-label="Faint hop cone illustration"></div>
    <div class="decor decor--mug-right" role="img" aria-label="Faint pixel beer mug illustration"></div>
    <div class="decor decor--hop-low" role="img" aria-label="Faint hop cone illustration"></div>

    <div class="brand">PVTR</div>
    <p class="tagline">PRESS START TO DRINK</p>
    <h2 class="style-name">PALE ALE</h2>
    <h1 class="product">BEER</h1>
    <p class="strength">13.37% ABV./VOL</p>
  </section>

  <section class="label label--pixel">
    <div class="skyline" role="img" aria-label="Pixel city skyline pattern"></div>
    <div class="decor decor--hop-top" role="img" aria-label="Faint hop cone illustration"></div>
    <div class="decor decor--mug-left" role="img" aria-label="Faint pixel beer mug illustration"></div>
    <div class="decor decor--hop-mid" role="img" aria-label="Faint hop cone illustration"></div>
    <div class="decor decor--mug-right" role="img" aria-label="Faint pixel beer mug illustration"></div>
    <div class="decor decor--hop-low" role="img" aria-label="Faint hop cone illustration"></div>

    <div class="brand">PVTR</div>
    <p class="tagline">PRESS START TO DRINK</p>
    <h2 class="style-name">PALE ALE</h2>
    <h1 class="product">BEER</h1>
    <p class="strength">13.37% ABV./VOL</p>
  </section>

</body>
</html>
```